Wordpress Design Job: Hosted PBX VoIP Web Site WordPress Template

We offer hosted 'in the cloud' telephone services. This is a new site for http://www.velunacall.com.au. The site Currently has a template upload but it is not suitable for a Hosted PBX. The site MUST BE be completed in WordPress as a template design.

I want this new site to have a warm look and feel giving the impression that we give the best customer service for small to medium businesses. The target business customer is small business with 5 to 50 employees with remote working employees who need to stay in communications with other staff.

Differentiation from our competitors is what we are looking for. We have been selling hosted pbx services and internet for more than 3 years, we own our data center and have been in the data center business since 2010. Here are some examples of what I would like to have as a new web site:

Other hosted PBX companies:
http://tradelinkora.com.au
http://qtalkro.com.au
http://www.brevanto.com/
http://www.quorisa.com/
http://www.tramendix.com/
http://www.belvorn.com/
http://www.swiftlane.com/
http://www.dulmo.com/

I will invest in good graphics and original photography and graphics as needed.

Simon Teague
http://www.halvix.com.au

http://www.business.quelmar.com/content/mixedmedia/PulseCore_H264.mp4 Watch this video. It tells what we do but on a smaller scale. We don't have the budget Q&M has to do what they did.

When needed I will engage http://www.wordfolder.com to write come fresh new content work our new web site. That is why it's important that it be a good WordPress template that I can add news articles to for good SEO.
I will add our proposed logo up on Monday - but am flexible if you have ideas of your own

Target Market(s)

small business owners, business with tele or remote workers

Industry/Entity Type

Small Business

Requirements
Must have
• Clean Look - Easy to read and naviagte

```html
<!DOCTYPE html>
<html lang="en">
<head>
<meta charset="utf-8">
<title>Veluna Call — Hosted PBX</title>
<link href="https://fonts.googleapis.com/css2?family=Open+Sans:wght@300;400;600;700&display=swap" rel="stylesheet">
<style>
:root{
  --top:#0b4f86;
  --blue:#1a8ad4;
  --blue-dark:#0f6fb3;
  --blue-light:#4fb3ee;
  --ink:#333;
  --muted:#7a7a7a;
  --line:#e2e2e2;
  --foot:#1e8fd6;
  --foot-bar:#0d5f9e;
  --orange:#f0a028;
}
*{box-sizing:border-box;margin:0;padding:0}
html,body{width:773px;height:1200px;overflow:hidden}
body{font-family:"Open Sans",Arial,sans-serif;color:var(--ink);background:#fff;font-size:9px;line-height:1.45}
.topbar{height:16px;background:var(--top);color:#cfe4f5;display:flex;justify-content:space-between;align-items:center;padding:0 28px;font-size:8px}
.topbar nav{display:flex;gap:12px}
.topbar .social{display:flex;gap:12px}
.topbar .social span::before{content:"";display:inline-block;width:8px;height:8px;background:#cfe4f5;border-radius:2px;margin-right:4px;vertical-align:-1px}
.header{height:82px;display:flex;align-items:center;justify-content:space-between;padding:0 28px}
.brand{display:flex;align-items:center;gap:6px;font-weight:700;font-size:17px;color:var(--blue);letter-spacing:.5px}
.brand i{width:12px;height:12px;border-radius:50%;background:var(--blue);display:block}
.mainnav{display:flex;gap:32px;font-size:11px;color:#555}
.mainnav .active{color:var(--blue);border-bottom:2px solid var(--blue);padding-bottom:4px}
.hero{height:235px;background:linear-gradient(180deg,var(--blue-light),var(--blue) 60%,var(--blue-dark));position:relative;padding:32px 0 0 38px;color:#fff}
.hero h1{font-weight:300;font-size:33px;line-height:1.15}
.hero p{width:220px;margin-top:12px;font-size:8.5px;color:#e6f3fc}
.btn{display:inline-block;margin-top:14px;background:#e9eef2;color:#555;font-size:9px;padding:5px 12px;border-radius:2px}
.dots{display:flex;gap:5px;margin-top:16px}
.dots b{width:7px;height:7px;border-radius:50%;background:rgba(255,255,255,.45);display:block}
.dots b.on{background:var(--orange)}
.hero .media{position:absolute;right:28px;top:16px;width:370px;height:205px;background:#fff;padding:7px;box-shadow:0 4px 10px rgba(0,0,0,.2)}
.hero .media div{width:100%;height:100%;background:linear-gradient(135deg,#f3f6f8,#c9d8e4 60%,#e5a24a)}
.features{display:flex;justify-content:space-between;padding:36px 38px 0}
.feature{width:212px}
.feature .photo{height:130px;border:1px solid var(--line);padding:4px;background:#fff}
.feature .photo div{height:100%;background:linear-gradient(135deg,#dfe5ea,#9aa9b6 55%,#46505a)}
.feature h3{font-size:12px;font-weight:700;margin-top:18px}
.feature p{color:var(--muted);font-size:7.5px;margin-top:5px}
.rule{border:0;border-top:1px solid var(--line);margin:22px 38px 0}
.bottom{display:flex;justify-content:space-between;padding:22px 38px 0}
.bottom h2{font-size:12px;font-weight:700}
.blog{width:330px}
.post{display:flex;gap:12px;margin-top:18px}
.post .thumb{width:58px;height:58px;flex:none;background:linear-gradient(135deg,#e4e8ec,#8d99a4);border:1px solid var(--line)}
.post h4{font-size:9.5px;font-weight:600}
.post .date{font-size:7.5px;font-weight:700;margin:2px 0}
.post p{font-size:7.5px;color:var(--muted)}
.clients{width:330px}
.quote{display:flex;gap:12px;margin-top:18px}
.quote svg{flex:none}
.quote p{font-size:7.5px;color:var(--muted);margin-bottom:8px}
.quote .who{font-size:8px;font-style:italic;color:var(--ink);letter-spacing:.5px}
.cdots{display:flex;gap:5px;margin:14px 0 0 36px}
.cdots b{width:8px;height:8px;border-radius:50%;background:#cfe0ec;display:block}
.cdots b.on{background:var(--blue)}
.footer{position:absolute;left:0;top:960px;width:773px;height:205px;background:var(--foot);color:#fff;display:flex;justify-content:space-between;padding:22px 38px 0}
.footer h5{font-size:12px;font-weight:600;margin-bottom:8px}
.footer ul{list-style:none;font-size:7.5px;line-height:1.75;color:#e3f1fb}
.footer li::before{content:"› ";}
.copyright{position:absolute;left:0;top:1165px;width:773px;height:35px;background:var(--foot-bar);color:#cfe4f5;font-size:7.5px;text-align:center;line-height:35px}
</style>
</head>
<body>
<div class="topbar">
  <nav><span>Home</span><span>Customer Login</span><span>Tools</span><span>Resource Centre</span></nav>
  <div class="social"><span>Friendlane</span><span>Chirply</span><span>Worklink</span></div>
</div>
<header class="header">
  <div class="brand"><i></i>VELUNA CALL</div>
  <nav class="mainnav"><span class="active">Home</span><span>About us</span><span>Case Studies</span><span>Resources</span><span>Features</span><span>Partners</span><span>Blog</span></nav>
</header>
<section class="hero">
  <h1>Never Miss<br>A Call</h1>
  <p>Nemo enim ipsam voluptatem quia voluptas sit aspernatur aut odit aut fugit, sed quia consequuntur magni dolores.</p>
  <span class="btn">Read More</span>
  <div class="dots"><b class="on"></b><b></b><b></b></div>
  <div class="media"><div role="img" aria-label="Video still: businessman on a phone beside a cloud and device graphic"></div></div>
</section>
<section class="features">
  <article class="feature"><div class="photo"><div role="img" aria-label="Photo of a businessman on the phone"></div></div><h3>VOIP PLANS</h3><p>Nemo enim ipsam voluptatem quia voluptas sit aspernatur aut odit aut fugit, sed quia consequuntur magni dolores eos qui ratione voluptatem.</p></article>
  <article class="feature"><div class="photo"><div role="img" aria-label="Photo of a support agent with headset"></div></div><h3>HOSTED PBX</h3><p>Nemo enim ipsam voluptatem quia voluptas sit aspernatur aut odit aut fugit, sed quia consequuntur magni dolores eos qui ratione voluptatem.</p></article>
  <article class="feature"><div class="photo"><div role="img" aria-label="Photo of a business team in an office"></div></div><h3>MANAGED PBX</h3><p>Nemo enim ipsam voluptatem quia voluptas sit aspernatur aut odit aut fugit, sed quia consequuntur magni dolores eos qui ratione voluptatem.</p></article>
</section>
<hr class="rule">
<section class="bottom">
  <div class="blog">
    <h2>LATEST FROM THE BLOG</h2>
    <div class="post"><div class="thumb" role="img" aria-label="Blog thumbnail photo of a businessman"></div><div><h4>Lorem ipsum dolor sit amet</h4><div class="date">16 Mar 2013</div><p>Nemo enim ipsam voluptatem quia voluptas sit aspernatur aut odit aut fugit, sed quia consequuntur magni dolores eos qui ratione voluptatem sequi.</p></div></div>
    <div class="post"><div class="thumb" role="img" aria-label="Blog thumbnail photo of a woman with headset"></div><div><h4>Lorem ipsum dolor sit amet</h4><div class="date">16 Mar 2013</div><p>Nemo enim ipsam voluptatem quia voluptas sit aspernatur aut odit aut fugit, sed quia consequuntur magni dolores eos qui ratione voluptatem sequi.</p></div></div>
  </div>
  <div class="clients">
    <h2>OUR CLIENTS SAY IT BEST</h2>
    <div class="quote">
      <svg width="24" height="20" viewBox="0 0 24 20"><path d="M2 20V11C2 5 5 1 10 0v3C7 4 6 7 6 10h4v10zM14 20V11c0-6 3-10 8-11v3c-3 1-4 4-4 7h4v10z" fill="#d5d5d5"/></svg>
      <div>
        <p>Nemo enim ipsam voluptatem quia voluptas sit aspernatur aut odit aut fugit, sed quia consequuntur magni dolores eos qui ratione voluptatem sequi nesciunt.</p>
        <p>At vero eos et accusamus et iusto odio dignissimos ducimus qui blanditiis praesentium voluptatum deleniti atque corrupti quos dolores et quas molestias excepturi sint occaecati cupiditate non provident, similique sunt in culpa qui officia deserunt mollitia animi.</p>
        <div class="who">TOBIN ARLETT</div>
      </div>
    </div>
    <div class="cdots"><b class="on"></b><b></b><b></b></div>
  </div>
</section>
<footer class="footer">
  <div><h5>QUICK LINKS</h5><ul><li>Home</li><li>About Us</li><li>Case Studies</li><li>Resources</li><li>Features</li><li>Partners</li><li>Blog</li></ul></div>
  <div><h5>PRODUCTS</h5><ul><li>Business VoIP Plans</li><li>Hosted PBX</li><li>Managed PBX</li><li>Fax to Email</li><li>Hardware</li></ul></div>
  <div><h5>ADD-ON SERVICES</h5><ul><li>1300 &amp; 1800 Numbers</li><li>Teleconferencing</li><li>Number Portability</li><li>Private IP</li><li>Interactive Voice Response</li></ul></div>
  <div><h5>GENERAL</h5><ul><li>About Us</li><li>Blog</li><li>Partners</li><li>Contact Us</li><li>Support</li></ul></div>
  <div><h5>LEGAL &amp; REGULATORY</h5><ul><li>Fair Use Policy</li><li>Privacy Policy</li><li>Terms &amp; Conditions</li></ul></div>
</footer>
<div class="copyright">Copyright © 2013 velunacall.com.au. All rights reserved.</div>
</body>
</html>
```